Design a Lumen Museum + exhibition design**

I'm creating an Online Museum for Hemp which will tell the story of hemp from ancient times to now and the future
cover the medical, industrial and nutritional uses and development of hemp
the people behind it, researchers, politicians, farmers and influencerts

the museum will have a number of "wings" , each holds an exhibition around a differnet theme, for example:

Hemp in the Age of Empires: 18th and 19th Century Collections
Hemp - The History of Healing
Domestication and Early Use: Ancient Collection
From Cotton Gin to Plastics and Prohibition: Hemp's Decline

these are just a few sample ideas for exhibitions

I'm looking for an overall design for the museum home page and exhibition page which will make people curious and want to spend time,learning and browsing

Think mobile -first :)

You are requested to design

1. Home page
2. Exhibition page

Target Market(s)

Hemp aficionados, curious fans

Logo Text

The Lumen Museum

Coding

Coded - Design and coding required

Number of Pages Required

3 page

Font styles to use
Sans Serif
Decorative

Requirements
Must have
• a homepage design which prompts visitors to immediately start watching an exhibition

visitors need to understand that this is a museum , so that they dont think it's a business, a service provider or anything like that

needs to have the usual links to T&C, privacy, about us

needs to have a link to "Wander past the lantern stall"

must have a visual WOW effect
Nice to have
• animations, sounds etc
Should not have
• forms like contact us etc - not relevant

```html
<!DOCTYPE html>
<html lang="en">
<head>
<meta charset="utf-8">
<title>The Lumen Museum — Exhibition</title>
<link href="https://fonts.googleapis.com/css2?family=Abril+Fatface&family=Libre+Baskerville&family=Poppins:wght@400;500;600&display=swap" rel="stylesheet">
<style>
  :root {
    --bg: #04141b;
    --bg-leaf: #163a26;
    --green: #5bd25f;
    --green-soft: #4cb351;
    --line: #2f7a3a;
    --white: #ffffff;
    --text-muted: #d5dbd8;
    --frame: #e8efe9;
    --art-warm: #f3ecc8;
    --art-green: #7fa24a;
  }
  * { box-sizing: border-box; margin: 0; padding: 0; }
  html, body { width: 1200px; height: 675px; overflow: hidden; background: var(--bg); }
  body { position: relative; font-family: "Poppins", sans-serif; color: var(--white); }

  .backdrop {
    position: absolute; inset: 0;
    background:
      radial-gradient(ellipse 180px 260px at 40px 430px, rgba(60,120,60,0.55), transparent 70%),
      radial-gradient(ellipse 420px 300px at 330px 200px, rgba(30,70,45,0.35), transparent 70%),
      radial-gradient(ellipse 420px 300px at 900px 120px, rgba(30,70,45,0.3), transparent 70%),
      var(--bg);
  }

  .brand { position: absolute; left: 87px; top: 33px; display: flex; align-items: center; gap: 6px; }
  .brand-mark { width: 28px; height: 28px; border: 1px solid var(--text-muted); border-radius: 50%; }
  .brand-name { font-family: "Libre Baskerville", serif; font-size: 13px; color: var(--white); }

  .shop-button { position: absolute; left: 984px; top: 25px; width: 132px; height: 43px; }
  .shop-button .outline { position: absolute; left: 0; top: 0; width: 127px; height: 37px; border: 1px solid var(--green); }
  .shop-button .fill {
    position: absolute; left: 5px; top: 6px; width: 127px; height: 37px;
    background: var(--green); color: var(--white);
    font-size: 10px; font-weight: 600; letter-spacing: 1px;
    display: flex; align-items: center; justify-content: center;
  }

  .headline {
    position: absolute; left: 0; width: 1200px; top: 92px; text-align: center;
    font-family: "Abril Fatface", serif; font-size: 41px; letter-spacing: 0.5px;
  }
  .headline .accent { color: var(--green); }
  .intro { position: absolute; left: 0; width: 1200px; top: 160px; text-align: center; font-size: 12px; color: var(--text-muted); }

  .timeline { position: absolute; left: 91px; top: 260px; width: 1109px; height: 1px; background: var(--line); }
  .timeline-start { position: absolute; left: 88px; top: 257px; width: 7px; height: 7px; border-radius: 50%; background: var(--green-soft); }

  .category { position: absolute; top: 232px; width: 120px; margin-left: -60px; text-align: center; font-size: 12px; font-weight: 500; color: var(--green-soft); }
  .stem { position: absolute; top: 252px; width: 1px; background: var(--line); }

  .exhibit { position: absolute; width: 244px; }
  .exhibit-frame { width: 244px; height: 163px; border: 1px solid var(--frame); padding: 2px; position: relative; }
  .exhibit-art { width: 100%; height: 100%; }
  .art-skull { background: radial-gradient(ellipse at 50% 55%, var(--art-green) 0%, #9bb25a 35%, var(--art-warm) 75%); }
  .art-flowers { background: radial-gradient(ellipse at 55% 40%, #e3cf48 0%, #b9c070 30%, #8fae62 55%, #ece4c8 90%); }
  .exhibit-frame.is-active .exhibit-art::after { content: ""; position: absolute; inset: 2px; background: rgba(20,40,35,0.72); }
  .learn-more {
    position: absolute; left: 58px; top: 62px; width: 127px; height: 38px; z-index: 2;
    background: var(--green); color: var(--white); font-size: 10px; font-weight: 600; letter-spacing: 0.8px;
    display: flex; align-items: center; justify-content: center;
  }
  .exhibit-caption { margin-top: 17px; text-align: center; font-size: 11px; line-height: 20px; color: var(--text-muted); }

  .social { position: absolute; left: 87px; top: 647px; display: flex; gap: 27px; }
  .social span { width: 9px; height: 9px; border-radius: 50%; background: var(--white); display: block; }

  .pager-dot { position: absolute; top: 645px; width: 5px; height: 5px; border-radius: 50%; background: var(--white); }
  .pager-dot.is-current { top: 642px; width: 11px; height: 11px; margin-left: -3px; background: none; border: 1px solid var(--white); }
  .pager-dot.is-current::after { content: ""; position: absolute; left: 2px; top: 2px; width: 5px; height: 5px; border-radius: 50%; background: var(--white); }

  .counter { position: absolute; right: 88px; top: 638px; font-size: 11px; font-weight: 500; }
  .counter .total { color: #9aa5a2; font-weight: 400; }
</style>
</head>
<body>
  <div class="backdrop" role="img" aria-label="Dark background of hemp leaves in shadow"></div>

  <header>
    <div class="brand"><span class="brand-mark"></span><span class="brand-name">The Lumen Museum</span></div>
    <div class="shop-button"><span class="outline"></span><span class="fill">GIFT SHOP</span></div>
  </header>

  <h1 class="headline"><span class="accent">The Exhibition</span> of Lumen Museum</h1>
  <p class="intro">Lorem ipsum dolor sit amet, consetetur sadipscing elitr, sed diam nonumy eirmod</p>

  <div class="timeline"></div>
  <div class="timeline-start"></div>

  <div class="category" style="left:273px">Painting</div>
  <div class="category" style="left:592px">Scupture</div>
  <div class="category" style="left:912px">Painting</div>
  <div class="stem" style="left:273px;height:35px"></div>
  <div class="stem" style="left:592px;height:85px"></div>
  <div class="stem" style="left:912px;height:35px"></div>

  <article class="exhibit" style="left:151px;top:303px">
    <div class="exhibit-frame is-active">
      <div class="exhibit-art art-skull" role="img" aria-label="Illustration of a hemp leaf artwork"></div>
      <span class="learn-more">LEARN MORE</span>
    </div>
    <p class="exhibit-caption">Greek anchors aweigh: powered by<br>Papyrus and Hemp</p>
  </article>

  <article class="exhibit" style="left:471px;top:352px">
    <div class="exhibit-frame">
      <div class="exhibit-art art-flowers" role="img" aria-label="Botanical illustration of flowering hemp plants"></div>
    </div>
    <p class="exhibit-caption">Greek anchors aweigh: powered by<br>Papyrus and Hemp</p>
  </article>

  <article class="exhibit" style="left:790px;top:303px">
    <div class="exhibit-frame">
      <div class="exhibit-art art-skull" role="img" aria-label="Illustration of a hemp leaf artwork"></div>
    </div>
    <p class="exhibit-caption">Greek anchors aweigh: powered by<br>Papyrus and Hemp</p>
  </article>

  <article class="exhibit" style="left:1109px;top:352px">
    <div class="exhibit-frame">
      <div class="exhibit-art art-flowers" role="img" aria-label="Botanical illustration of flowering hemp plants"></div>
    </div>
    <p class="exhibit-caption">Greek anchors aweigh: powered by<br>Papyrus and Hemp</p>
  </article>

  <nav class="social" aria-label="Social links"><span></span><span></span><span></span></nav>

  <div class="pager-dot is-current" style="left:463px"></div>
  <div class="pager-dot" style="left:553px"></div>
  <div class="pager-dot" style="left:646px"></div>
  <div class="pager-dot" style="left:738px"></div>

  <div class="counter">01 / <span class="total">04</span></div>
</body>
</html>
```